Label design for an exciting new Vodka brand

We need a label design for a dynamic new Vodka brand called 'Pale lantern Vodka'. It is a crisp and versatile liquid with a clean and smooth finish. It should appeal to 21-39 year olds, with a slight female skew. Colours, fonts and styles should be modern and relatively neutral - take inspiration from the brand pictures attached.

Target Market(s)

21-39 year olds, both male and female, but with a slight female skew

```html
<!DOCTYPE html>
<html lang="en">
<head>
<meta charset="utf-8">
<title>Pale lantern Vodka – Label Spec</title>
<link href="https://fonts.googleapis.com/css2?family=Great+Vibes&family=Montserrat:wght@400;500;600&display=swap" rel="stylesheet">
<style>
  :root {
    --blush: #F0C2D4;
    --ink: #111111;
    --paper: #ffffff;
    --trim: #e0403f;
    --tag-pink: #e9a3bd;
    --emboss-light: rgba(255,255,255,0.75);
    --emboss-shadow: rgba(190,130,155,0.55);
    --silver-hi: #d8d8d8;
    --silver-mid: #9a9a9a;
    --silver-lo: #6f6f6f;
  }
  * { box-sizing: border-box; margin: 0; padding: 0; }
  html, body {
    width: 1200px; height: 1086px; overflow: hidden;
    background: var(--paper);
    font-family: 'Montserrat', sans-serif;
    color: var(--ink);
  }
  .sheet { position: relative; width: 1200px; height: 1086px; }

  .dimension {
    position: absolute; font-size: 20px; color: var(--ink);
  }
  .dimension--width { left: 560px; top: 36px; }
  .dimension--height { left: 44px; top: 540px; }

  .label {
    position: absolute; left: 173px; top: 95px;
    width: 798px; height: 943px;
    border: 2px solid var(--trim);
    background: var(--paper);
    overflow: hidden;
  }
  .label__panel {
    position: absolute; left: 0; top: 0; width: 100%; height: 697px;
    background: var(--blush);
  }
  .brand-mark {
    position: absolute; left: 287px; top: 44px;
    width: 224px; text-align: center;
  }
  .brand-mark__circle {
    width: 180px; height: 180px; margin: 0 auto;
    border-radius: 50%;
    border: 4px solid var(--emboss-light);
    box-shadow: 2px 3px 3px var(--emboss-shadow), inset 2px 3px 3px var(--emboss-shadow);
  }
  .brand-mark__name {
    margin-top: 14px; font-size: 24px; font-weight: 500;
    letter-spacing: 3px; color: var(--emboss-light);
    text-shadow: 1px 2px 2px var(--emboss-shadow);
  }
  .name-script {
    position: absolute; left: 90px; top: 350px;
    font-family: 'Great Vibes', cursive;
    font-size: 96px; color: var(--paper);
    text-shadow: 1px 2px 3px var(--emboss-shadow);
    line-height: 1;
  }
  .name-foil {
    position: absolute; left: 0; width: 100%; top: 455px;
    text-align: center;
    font-size: 140px; font-weight: 600; letter-spacing: 2px;
    line-height: 1;
    background: linear-gradient(180deg, var(--silver-hi) 0%, var(--silver-mid) 45%, var(--silver-lo) 55%, var(--silver-hi) 100%);
    -webkit-background-clip: text; background-clip: text;
    color: transparent;
  }
  .product {
    position: absolute; left: 0; width: 100%; top: 735px;
    text-align: center; font-size: 64px; font-weight: 500;
    letter-spacing: 10px; line-height: 1;
  }
  .tagline {
    position: absolute; left: 0; width: 100%; top: 802px;
    text-align: center; font-size: 17px; letter-spacing: 3px;
    color: var(--tag-pink);
  }
  .facts {
    position: absolute; left: 36px; right: 36px; top: 838px;
    border-top: 2px solid var(--ink);
    display: flex; justify-content: center; align-items: center;
    padding-top: 22px; font-size: 18px;
  }
  .facts__item { padding: 0 14px; line-height: 1.3; }
  .facts__item + .facts__item { border-left: 2px solid var(--ink); }

  .spec {
    position: absolute; left: 1018px; top: 100px;
    font-size: 17px; line-height: 33px; color: var(--ink);
  }
  .spec__heading { text-decoration: underline; text-underline-offset: 4px; }
  .spec__group { margin-bottom: 32px; }
</style>
</head>
<body>
<main class="sheet">
  <span class="dimension dimension--width">90</span>
  <span class="dimension dimension--height">120</span>

  <section class="label" aria-label="Pale lantern Vodka label">
    <div class="label__panel">
      <div class="brand-mark">
        <div class="brand-mark__circle"></div>
        <div class="brand-mark__name">Pale lantern</div>
      </div>
      <div class="name-script">Pale</div>
      <div class="name-foil">LANTERN</div>
    </div>
    <h1 class="product">VODKA</h1>
    <p class="tagline">GO ON. LIGHT YOUR OWN LANTERN.</p>
    <div class="facts">
      <span class="facts__item">NET.WT.700 ML</span>
      <span class="facts__item">CLEAN AND SMOOTH FINISH</span>
      <span class="facts__item">40% ALC/VOL</span>
    </div>
  </section>

  <aside class="spec">
    <div class="spec__group">
      <div>COLORS:</div>
      <div>#F0C2D4</div>
      <div>&nbsp;BLACK</div>
    </div>
    <div class="spec__group">
      <div class="spec__heading">EMBOSSING</div>
      <div>LOGO</div>
      <div>PALE</div>
      <div>VODKA</div>
    </div>
    <div class="spec__group">
      <div class="spec__heading">SPOT UV &amp; SILVER FOIL</div>
      <div>LANTERN</div>
    </div>
  </aside>
</main>
</body>
</html>
```